Neue Website fuer Software-Firma (CMS: Joomla, Responsive Design)
Zielgruppe
Die VANTRIX ist ein Software- und Beratungshaus im Lager- und Produktionslogistikbereich. Unsere Kunden sind Industriefirmen und Logistikdienstleister, die ein oder mehrere Laeger bewirtschaften und dafuer eine Software und mobile Datenerfassung einsetzen. Fast alle unserer Kunden haben KVT im Einsatz.
Aufgabenstellung
Unsere aktuelle Website wurde seit langem nicht mehr gepflegt und ist veraltet.
Wir moechten die neue Website gern mit dem CMS Joomla betreiben (ggf. waere auch Wordpress moeglich). Gern koennen Sie als Basis ein bereits existierendes (freies) Theme verwenden, wenn es entweder bereits alle Ansprueche erfuellt oder Sie es entsprechend anpassen.
Die neue Website soll in jedem Fall responsive sein, d.h. sowohl auf Desktop, Tablet und Smartphone funktionieren und das Design entsprechend anpassen.
Unsere aktuelle Seite steht unter www.vantrix-lagerwerk.example
Eine Seite, die uns besonders gut gefaellt, ist www.quendal.example (die sich auch teilweise an die gleichen Kunden richtet).
Wir moechten ein klares Design. Ein Beispiel, wie eines unserer Dashboards unserer Software aussieht, finden Sie anbei. Die Farbgestaltung darin wird jedoch noch geaendert. Sie wird eher in Richtung der Farbgestaltung der Quendal-Website gehen, jedoch immer noch grundsaetzlich hell sein. Evtl. koennen Sie Elemente daraus aufgreifen? Es soll in jedem Fall ersichtlich sein, dass Website und Software von der gleichen Firma sind.
Es soll moeglichst viel mit Grafiken gearbeitet werden – aehnlich der Quendal-Seite unter der Dia-Show. Diese muessen aber nicht zwingend farbig sein. Ein Mockup fuer einfarbige Grafiken unterhalb einer Diashow habe ich hier erstellt: https://helgard07.seitenbau.example/meinewebsite-1 Bitte orientieren Sie sich aber nicht an dieser Seite selbst – das war nur ein Probierbeispiel.
Desweiteren soll die Seite suchmaschinenfreundlich sein.
In Ihren Leistungen enthalten sein soll:
- Erstellung der Homepage incl.
o Menu (wie bei Quendal soll es ausklappbar sein und mind. 2 Ebenen koennen)
o Login-Button der einen externen Link aufruft
o Auswahl der Sprache (und damit Verlinkung zu jeweils der Homepage in der
ausgewaehlten Sprache
o Moeglichkeit zum Chat
o Suchfeld zum Durchsuchen aller S..

```html
<!DOCTYPE html>
<html lang="en">
<head>
<meta charset="utf-8">
<title>VANTRIX – Software Solutions for Logistics</title>
<link href="https://fonts.googleapis.com/css2?family=Lato:ital,wght@0,300;0,400;0,700;1,300&display=swap" rel="stylesheet">
<style>
:root{
  --navy:#1d3a84;
  --navy-deep:#152d6e;
  --red:#cc0000;
  --ink:#444a55;
  --muted:#8a8f99;
  --page:#f6f6f7;
  --header:#eff2f5;
  --footer:#1b2030;
  --footer-text:#c9ccd3;
  --line:#d8dbe0;
  --social:#8b95aa;
  --white:#ffffff;
}
*{margin:0;padding:0;box-sizing:border-box}
html,body{width:1178px;height:1200px;overflow:hidden}
body{font-family:'Lato',sans-serif;color:var(--ink);background:var(--page);position:relative}
.abs{position:absolute}

/* header */
.site-header{position:absolute;left:0;top:0;width:1178px;height:55px;background:var(--header);border-bottom:1px solid var(--red)}
.brand{left:238px;top:16px;font-size:22px;font-weight:400;color:var(--navy);letter-spacing:.5px}
.sep{top:0;width:1px;height:54px;background:var(--line)}
.menu-toggle{left:372px;top:19px;display:flex;align-items:center;gap:11px;font-size:12px;color:var(--navy-deep)}
.menu-toggle .bars{width:24px;height:17px;display:flex;flex-direction:column;justify-content:space-between}
.menu-toggle .bars span{height:3px;background:#222a3a}
.util{top:19px;display:flex;align-items:center;gap:7px;font-size:10px;color:#555c68}
.social{left:888px;top:18px;display:flex;gap:2px}
.social span{width:18px;height:18px;display:block;background:var(--social)}

/* hero */
.hero{left:0;top:55px;width:1178px;height:384px;background:radial-gradient(ellipse at 72% 45%,#3a67b8 0%,#1f4597 40%,#17367f 100%)}
.hero h1{position:absolute;left:272px;top:128px;font-weight:300;font-size:34px;line-height:36px;color:var(--white)}
.btn-contact{position:absolute;left:276px;top:229px;width:160px;height:31px;background:var(--red);color:var(--white);font-size:15px;font-weight:300;display:flex;align-items:center;justify-content:center}
.dots{position:absolute;left:571px;top:361px;display:flex;gap:5px}
.dots span{width:5px;height:5px;border-radius:50%;background:#aab7d8}
.dots span:first-child{background:var(--white)}

/* expertise */
.experts{left:0;top:439px;width:1178px;height:77px;background:var(--white);box-shadow:0 3px 6px rgba(0,0,0,.06)}
.experts-title{position:absolute;left:0;top:0;width:350px;height:77px;background:var(--red);color:var(--white);font-size:18px;font-weight:300;line-height:22px;padding:16px 0 0 243px}
.skill{position:absolute;top:17px;width:120px;text-align:center;font-size:9.5px;letter-spacing:.8px;color:#3d4656}
.skill svg{display:block;margin:0 auto 5px}

/* about */
.about-title{left:245px;top:579px;font-size:22px;font-weight:300;line-height:27px;color:var(--navy)}
.about-lead{left:247px;top:641px;font-size:11.5px;font-style:italic;font-weight:300;line-height:15px;color:var(--muted)}
.about-body{left:247px;top:689px;width:172px;font-size:9.6px;line-height:11.8px;color:#4c525d;font-weight:300}
.read-more{left:247px;top:802px;font-size:9.5px;color:var(--navy);display:flex;align-items:center;gap:6px}
.read-more::before{content:"";width:4px;height:4px;background:var(--red)}
.card{top:568px;width:151px;height:251px;background:var(--white);box-shadow:0 1px 4px rgba(0,0,0,.08)}
.card .photo{height:136px}
.card h3{font-size:11px;font-weight:400;color:var(--navy);margin:12px 0 0 12px}
.card p{font-size:9.5px;line-height:11.8px;font-weight:300;color:#4c525d;margin:6px 12px 0 12px}

/* clients */
.clients{left:0;top:877px;width:1178px;height:67px;background:var(--white);border-top:1.5px solid var(--navy-deep)}
.client-row{position:absolute;left:318px;top:22px;width:584px;display:flex;justify-content:space-between;align-items:center}
.client-row span{font-size:14px;color:#c3c6cc;letter-spacing:.5px}

/* footer */
.site-footer{left:0;top:944px;width:1178px;height:256px;background:var(--footer);color:var(--footer-text)}
.site-footer h2{position:absolute;font-size:16px;font-weight:300;color:#e1e3e8}
.field{position:absolute;border-bottom:1px solid #3f4558;font-size:9px;font-style:italic;font-weight:300;color:#7a8091;padding-bottom:4px}
.btn-send{position:absolute;left:500px;top:142px;width:54px;height:23px;border:1px solid var(--red);color:var(--red);font-size:9.5px;display:flex;align-items:center;justify-content:center}
.office{position:absolute;top:62px;font-size:9.5px;line-height:11.8px;font-weight:300;color:#d6d8de}
.office .tag{display:inline-block;background:var(--red);color:var(--white);font-size:9.5px;padding:3px 5px;margin-bottom:9px;font-weight:400}
.office .mail{color:var(--red)}
.footer-nav{position:absolute;left:251px;top:234px;display:flex;gap:10px;font-size:9.5px;font-weight:300;color:#d6d8de}
.copyright{position:absolute;left:767px;top:234px;font-size:9.5px;font-weight:300;color:#5c6275}
</style>
</head>
<body>

<header class="site-header">
  <div class="abs brand">VANTRIX</div>
  <div class="abs sep" style="left:357px"></div>
  <div class="abs menu-toggle"><div class="bars"><span></span><span></span><span></span></div>Menu</div>
  <div class="abs sep" style="left:447px"></div>
  <div class="abs util" style="left:698px">
    <svg width="16" height="17" viewBox="0 0 16 17" fill="none" stroke="#6b7280" stroke-width="1"><circle cx="8" cy="5" r="4"/><path d="M1 16c0-4 3-6 7-6s7 2 7 6z"/></svg>Login
  </div>
  <div class="abs util" style="left:777px">
    <svg width="16" height="16" viewBox="0 0 16 16" fill="none" stroke="#6b7280" stroke-width="1"><circle cx="8" cy="8" r="7"/><path d="M1 8h14M8 1c3 3 3 11 0 14M8 1c-3 3-3 11 0 14"/></svg>Language
  </div>
  <div class="abs social" aria-label="Social links">
    <span></span><span></span><span></span>
  </div>
</header>

<section class="abs hero" role="img" aria-label="Blue background with a network of connected glowing dots and lines">
  <h1>We are conectiong dots in<br>your logistic business</h1>
  <div class="btn-contact">CONTACT US</div>
  <div class="dots"><span></span><span></span><span></span><span></span></div>
</section>

<section class="abs experts">
  <div class="experts-title">We are<br>Experts in:</div>
  <div class="skill" style="left:392px">
    <svg width="26" height="26" viewBox="0 0 26 26" fill="none" stroke="#3d4656" stroke-width="1.2"><path d="M1 9l12-7 12 7v15H1z"/><path d="M4 24V12h18v12M8 15h10M8 18h10M8 21h10"/></svg>PRODUCTION
  </div>
  <div class="skill" style="left:531px">
    <svg width="26" height="26" viewBox="0 0 26 26" fill="none" stroke="#3d4656" stroke-width="1.2"><rect x="1" y="3" width="24" height="20"/><path d="M1 10h24M10 3v9h6V3"/><rect x="16" y="16" width="6" height="4"/></svg>WAREHOUSING
  </div>
  <div class="skill" style="left:669px">
    <svg width="32" height="26" viewBox="0 0 32 26" fill="none" stroke="#3d4656" stroke-width="1.2"><path d="M8 22a6 6 0 010-12 9 9 0 0117-2 6 6 0 011 14z"/><path d="M16 13l5 2.5v5L16 23l-5-2.5v-5zM11 15.5l5 2.5 5-2.5M16 18v5"/></svg>KVT
  </div>
  <div class="skill" style="left:808px">
    <svg width="30" height="26" viewBox="0 0 30 26" fill="none" stroke="#3d4656" stroke-width="1.2"><rect x="2" y="19" width="26" height="5"/><circle cx="7" cy="21.5" r="1"/><circle cx="15" cy="21.5" r="1"/><circle cx="23" cy="21.5" r="1"/><path d="M6 19V9l8-6 5 4M19 7v6M14 3l1-2"/><rect x="17" y="13" width="5" height="6"/></svg>AUTOMATION
  </div>
</section>

<h2 class="abs about-title">Über<br>VANTRIX Inc.</h2>
<p class="abs about-lead">Our top goal is clearly defined:<br>your satisfaction.</p>
<p class="abs about-body">We develop an optimal solution based on your specific internal logistics require­ments. Our company will collaborate with you on the operational and techni­cal requirements of your business and implement a software solution – either stand alone or integrated with your KVT® system.</p>
<div class="abs read-more">Read Mroe</div>

<article class="abs card" style="left:460px">
  <div class="photo" role="img" aria-label="Worker scanning boxes in a warehouse" style="background:linear-gradient(135deg,#c9b08a,#8fa6c6 60%,#e2e6ec)"></div>
  <h3>KVT Development</h3>
  <p>Explore the world of mobile data entry in KVT WM, IM and SD with customized mobile apps for barcode scanners, tablets or smart phones.</p>
</article>
<article class="abs card" style="left:624px">
  <div class="photo" role="img" aria-label="Warehouse worker with laptop between stacked goods" style="background:linear-gradient(135deg,#8a5a3a,#c9a27a 45%,#7590b8)"></div>
  <h3>Warehouse Management</h3>
  <p>Discover the comprehensive tool box for different warehouse processes incl. receiving, staging, picking, packing, shipping, labeling...</p>
</article>
<article class="abs card" style="left:787px">
  <div class="photo" role="img" aria-label="Automated robot carrying a yellow storage shelf" style="background:linear-gradient(180deg,#d9d23a,#b7b12c 60%,#3b3b3e)"></div>
  <h3>Automation / Integration</h3>
  <p>Looking for integrating print&amp;apply systems, conveyors, fix mounted scanners, sorters etc. directly into your KVT system?</p>
</article>

<section class="abs clients" aria-label="Clients">
  <div class="client-row">
    <span>Arvelo</span><span>Tesmar</span><span>Kornwald</span><span>Lindhof</span><span>Mirelle</span><span>Sorvane</span><span>Talvik</span>
  </div>
</section>

<footer class="abs site-footer">
  <h2 style="left:244px;top:20px">Drop us a line</h2>
  <div class="field" style="left:246px;top:67px;width:146px">Full name</div>
  <div class="field" style="left:406px;top:67px;width:147px">Email</div>
  <div class="field" style="left:246px;top:108px;width:307px">Your message</div>
  <div class="btn-send">SEND</div>

  <h2 style="left:608px;top:20px">Contact Information</h2>
  <div class="office" style="left:610px">
    <span class="tag">USA</span><br>
    VANTRIX -<br>Software Solutions For Logistics, Inc.<br>240 W Harlow Ave., Suite 310<br>Brentfield, MI 48990<br>
    <span class="mail">info@vantrix-lagerwerk.example</span><br>Tel: +1 555 010 4471<br>Fax: +1 555 010 2286
  </div>
  <div class="office" style="left:795px">
    <span class="tag">GER</span><br>
    VANTRIX GmbH -<br>Softwareloesungen der Logistik<br>Werkstrasse 14<br>61999 Hallberg<br>
    <span class="mail">info@vantrix-lagerwerk.example</span><br>Tel: +49 555 01400<br>Fax: +49 555 014029
  </div>

  <nav class="footer-nav"><span>About us</span><span>Services</span><span>Contact</span><span>Career</span><span>News</span><span>Blog</span><span>Impring</span><span>AGB</span></nav>
  <div class="copyright">© 2017 by VANTRIX GmbH / VANTRIX Inc.</div>
</footer>

</body>
</html>
```